Teskar Business Cards

We need new Business Cards for our startup. It just launched.It is working in the high-end it-market. Specifically in the cloud area. We are a hybrid cloud company. The company logo is attached. We are a Swiss based company. Information visible on the card is: 1. Logo 2. Company Name: Teskar AG 3. Subtitle: Hybrid Clouds. 3. Name: Lukas Brenner 4. Adress: Holderweg 12a, 8462 Mersenau, Veldria 5. Email: lukas@teskar.example. 6. Mobile: +41 79 304 62 18. It should be a grey/white design. Similar to the attached logo. It should have class, high-quality but not too much color and no gold used.

I forgot to add my Position. Please use Founder / CEO. thanks lukas

```html
<!DOCTYPE html>
<html lang="en">
<head>
<meta charset="utf-8">
<title>Teskar AG – Business Card</title>
<link href="https://fonts.googleapis.com/css2?family=Lato:wght@400;700&display=swap" rel="stylesheet">
<style>
  :root {
    --backdrop: #e3e3e3;
    --card: #f9f9f9;
    --band: #5e5e5e;
    --ink-strong: #474747;
    --ink: #555555;
    --ink-soft: #666666;
    --rule: #ffffff;
  }
  * { margin: 0; padding: 0; box-sizing: border-box; }
  html, body {
    width: 1200px;
    height: 900px;
    overflow: hidden;
    background: var(--backdrop);
    font-family: "Lato", sans-serif;
  }
  .business-card {
    position: absolute;
    left: 150px;
    top: 170px;
    width: 900px;
    height: 560px;
    background: var(--card);
    box-shadow: 0 6px 18px rgba(0,0,0,0.18);
    overflow: hidden;
  }
  .brand {
    position: absolute;
    left: 90px;
    top: 150px;
    display: flex;
    align-items: center;
    gap: 22px;
  }
  .brand-mark {
    width: 14px;
    height: 14px;
    border-radius: 50%;
    background: var(--ink-soft);
  }
  .brand-name {
    font-weight: 400;
    font-size: 34px;
    letter-spacing: 0.55em;
    color: var(--ink-soft);
  }
  .contact {
    position: absolute;
    left: 560px;
    top: 175px;
    color: var(--ink);
  }
  .person-name {
    font-weight: 700;
    font-size: 29px;
    color: var(--ink-strong);
    letter-spacing: 0.01em;
    line-height: 1.05;
  }
  .person-role {
    font-size: 20px;
    color: var(--ink-soft);
    margin-bottom: 26px;
  }
  .address {
    font-size: 20px;
    line-height: 1.3;
    color: var(--ink-soft);
    margin-bottom: 12px;
    font-style: normal;
  }
  .contact-line {
    display: flex;
    align-items: center;
    gap: 12px;
    font-size: 20px;
    line-height: 1.35;
    color: var(--ink-soft);
  }
  .contact-line svg { width: 20px; height: 20px; flex: none; }
  .footer-band {
    position: absolute;
    left: 0;
    bottom: 0;
    width: 100%;
    height: 118px;
    background: var(--band);
    display: flex;
    align-items: center;
    padding: 0 40px 20px 34px;
    color: var(--rule);
  }
  .company {
    font-weight: 700;
    font-size: 24px;
    white-space: nowrap;
  }
  .tagline {
    font-size: 19px;
    margin-left: 8px;
    white-space: nowrap;
  }
  .band-rule {
    flex: 1;
    height: 2px;
    background: var(--rule);
    margin-left: 16px;
    margin-top: 18px;
  }
</style>
</head>
<body>
  <section class="business-card">
    <div class="brand">
      <span class="brand-mark"></span>
      <span class="brand-name">TESKAR</span>
    </div>

    <div class="contact">
      <div class="person-name">LUKAS BRENNER</div>
      <div class="person-role">Founder / CEO</div>
      <address class="address">Holderweg 12a<br>8462 Mersenau, Veldria</address>
      <div class="contact-line">
        <svg viewBox="0 0 20 20" aria-hidden="true">
          <rect x="5" y="1.5" width="10" height="17" rx="2" fill="none" stroke="#444" stroke-width="1.6"/>
          <line x1="8.5" y1="15.5" x2="11.5" y2="15.5" stroke="#444" stroke-width="1.4"/>
        </svg>
        <span>+41 79 304 62 18</span>
      </div>
      <div class="contact-line">
        <svg viewBox="0 0 20 20" aria-hidden="true">
          <rect x="1.5" y="4" width="17" height="12" fill="#444"/>
          <polyline points="1.5,4 10,11 18.5,4" fill="none" stroke="#f9f9f9" stroke-width="1.3"/>
        </svg>
        <span>lukas@teskar.example</span>
      </div>
    </div>

    <div class="footer-band">
      <span class="company">TESKAR AG -</span>
      <span class="tagline">Hybrid Clouds</span>
      <span class="band-rule"></span>
    </div>
  </section>
</body>
</html>
```